Webdesign für Arztpraxis
Zielgruppe
Arztpraxis für Dermatologie am Lindenhof.
Lindenhof ist ein Spital/Krankenhaus hier in Basel, Schweiz.
Kunden sind in jeder Altersstufe für Hauterkrankungen.
Behandlung Chirugisch, konservativ und mit Laser.
Aufgabenstellung
Brandguide und Logo anbei
Farben: #395722 und #ABCF8A
Beispielseite, die gefällt: https://hautpraxis-brunner-kessler.example

```html
<!DOCTYPE html>
<html lang="de">
<head>
<meta charset="utf-8">
<title>Dermatologie am Lindenhof – Startseite</title>
<link href="https://fonts.googleapis.com/css2?family=Poppins:wght@400;500;600;700&display=swap" rel="stylesheet">
<style>
:root{
  --green-dark:#395722;
  --green-light:#ABCF8A;
  --green-accent:#7dba52;
  --band:#e5f0da;
  --ink:#1b1b1b;
  --muted:#6b6b6b;
  --white:#ffffff;
  --teal:#1aa59a;
}
*{box-sizing:border-box;margin:0;padding:0}
html,body{width:1200px;height:1200px;overflow:hidden;background:#fff}
body{font-family:'Poppins',sans-serif;color:var(--ink);position:relative}
.page{position:absolute;left:300px;top:30px;width:966px;height:1883px;transform:scale(.6211);transform-origin:0 0;overflow:hidden;background:#fff}
.abs{position:absolute}
.hero-photo{left:0;top:0;width:966px;height:492px;background:linear-gradient(100deg,#b7a58a 0%,#d9d6d0 20%,#e9e6e2 45%,#9eb08e 62%,#3f6b3a 80%,#2e5230 100%)}
.header{left:133px;top:9px;width:699px;height:56px;background:var(--white);border-radius:5px;box-shadow:0 2px 8px rgba(0,0,0,.15)}
.brand-dot{left:10px;top:8px;width:40px;height:40px;border-radius:50%;background:var(--green-dark)}
.brand-name{left:62px;top:6px;font-size:24px;line-height:26px;font-weight:500;color:var(--green-dark)}
.brand-sub{left:62px;top:32px;font-size:15px;font-weight:500;color:var(--green-dark)}
.nav{left:243px;top:38px;display:flex;gap:13px;font-size:8.5px;font-weight:500}
.nav .active{color:var(--green-accent);border-bottom:1px solid var(--green-accent);padding-bottom:2px}
.info{font-size:6.5px;line-height:7px;color:#333}
.info svg{position:absolute;left:-17px;top:0}
.btn-outline{border:1px solid var(--green-light);border-radius:14px;color:var(--green-accent);font-size:8px;display:flex;align-items:center;justify-content:center;gap:22px;background:var(--white)}
.welcome{left:474px;top:108px;width:266px;height:266px;border-radius:50%;background:var(--white);text-align:center}
.welcome-ring{left:464px;top:98px;width:286px;height:286px;border-radius:50%;border:1px dashed rgba(255,255,255,.9)}
.welcome h1{margin-top:34px;font-size:22px;line-height:27.5px;font-weight:700}
.btn-dark{left:88px;top:215px;width:84px;height:23px;border-radius:12px;background:var(--green-dark);color:#fff;font-size:9px;display:flex;align-items:center;justify-content:center}
.slide-prev{left:21px;top:220px;width:50px;height:50px;border-radius:50%;background:rgba(120,110,100,.55)}
.band{left:0;width:966px;background:var(--band)}
.quick{top:471px;width:167px;height:43px;background:var(--white);border-radius:22px;box-shadow:0 3px 6px rgba(0,0,0,.12);display:flex;align-items:center;font-size:9.5px;font-weight:600;color:var(--green-dark);padding:0 12px}
.quick .label{flex:1;text-align:left}
.arch{width:175px;height:224px;border-radius:88px 0 0 0;background:linear-gradient(180deg,#e6ebe3 0%,#c9b7a6 45%,#24242c 100%)}
.photo{background:linear-gradient(120deg,#d8d0c2,#b9c6d8 45%,#8aa37d)}
.eyebrow{font-size:6.5px;color:var(--green-accent)}
.h2{font-size:16px;font-weight:600}
.body{font-size:8px;line-height:12.8px;color:#333;width:285px}
.center{text-align:center;width:966px;left:0}
.sec-title{font-size:12px;font-weight:600}
.service img,.thumb{width:116px;height:116px;border-radius:6px}
.cap-title{font-size:8px;color:var(--green-accent);font-weight:500}
.cap-more{font-size:7.5px;color:var(--muted)}
.circ-arrow{width:16px;height:16px;border-radius:50%;background:#d8d8d8}
.dots{display:flex;gap:4px;justify-content:center}
.dots span{width:6px;height:6px;border-radius:50%;background:#d9d9d9}
.dots span:first-child{background:#b5b5b5}
.card{top:1255px;width:166px;height:194px;background:#fff;border:1px solid #ececec;box-shadow:0 1px 4px rgba(0,0,0,.08);text-align:center}
.card .icon{left:46px;top:-31px;width:74px;height:74px;border-radius:50%}
.card h3{margin-top:52px;font-size:9px;font-weight:600}
.card p{margin:6px 8px 0;font-size:7.6px;line-height:12.8px;color:#333}
.card .more{left:45px;top:164px;width:77px;height:22px;border:1px solid var(--teal);border-radius:12px;color:var(--teal);font-size:8px;display:flex;align-items:center;justify-content:center;gap:18px}
.btn-teal{border:1px solid var(--teal);color:var(--teal);border-radius:12px;font-size:8px;display:flex;align-items:center;justify-content:center;gap:6px}
</style>
</head>
<body>
<div class="page">
  <!-- Hero -->
  <div class="abs hero-photo" role="img" aria-label="Foto: weisse Praxisgebäude mit Bäumen"></div>
  <div class="abs slide-prev"><svg width="50" height="50"><path d="M28 15 L19 25 L28 35" fill="none" stroke="#fff" stroke-width="1.5"/></svg></div>
  <svg class="abs" style="left:910px;top:233px" width="16" height="24"><path d="M4 2 L13 12 L4 22" fill="none" stroke="#fff" stroke-width="1.5"/></svg>

  <header class="abs header">
    <div class="abs brand-dot"></div>
    <div class="abs brand-name">Dermatologie</div>
    <div class="abs brand-sub">am Lindenhof</div>
    <nav class="abs nav"><span class="active">Home</span><span>Über Uns</span><span>Leistungsspektrum</span><span>Kontakt</span></nav>
    <div class="abs info" style="left:388px;top:17px">
      <svg width="13" height="13"><circle cx="6.5" cy="6.5" r="5.5" fill="none" stroke="var(--green-accent)"/><path d="M6.5 3.5V6.5H9" fill="none" stroke="var(--green-accent)"/></svg>
      MO. – FR.<br>10–17 Uhr</div>
    <div class="abs info" style="left:503px;top:17px">
      <svg width="13" height="13"><path d="M2 2c0 5 4 9 9 9l1-2-2.5-1.5L8 9C6 8 5 7 4 5l1.5-1.5L4 1z" fill="none" stroke="var(--green-accent)"/></svg>
      Telefon<br>05 000 22233</div>
    <div class="abs btn-outline" style="left:571px;top:10px;width:122px;height:23px">Online Termin <span>→</span></div>
  </header>

  <div class="abs welcome-ring"></div>
  <div class="abs welcome">
    <h1>Herzlich<br>willkommen<br>in der Hautarztpraxis<br>im Rosental-Quartier<br>Basel!</h1>
    <div class="abs btn-dark">Termin online</div>
  </div>

  <!-- About band -->
  <div class="abs band" style="top:492px;height:312px"></div>
  <div class="abs quick" style="left:133px"><svg width="20" height="20" style="margin-right:6px"><rect x="2" y="4" width="15" height="13" rx="2" fill="none" stroke="var(--green-dark)"/><path d="M2 8H17M6 2V5M13 2V5" stroke="var(--green-dark)"/></svg><span class="label">Termine Buchen</span>→</div>
  <div class="abs quick" style="left:311px"><svg width="20" height="20" style="margin-right:6px"><path d="M3 3c0 8 6 14 14 14l1-3-4-2-2 2c-3-1-5-3-6-6l2-2L6 2z" fill="none" stroke="var(--green-dark)"/></svg><span class="label">Arzt auf Abruf</span>→</div>
  <div class="abs quick" style="left:488px;padding-left:44px"><span class="label">Anfahrt</span>→</div>
  <div class="abs quick" style="left:665px;padding-left:44px"><span class="label">Öffnungszeiten</span>→</div>

  <div class="abs arch" style="left:133px;top:548px" role="img" aria-label="Porträtfoto des Praxisinhabers"></div>
  <div class="abs eyebrow" style="left:329px;top:560px">Über Uns</div>
  <div class="abs h2" style="left:329px;top:569px">Dermatologie am Lindenhof</div>
  <p class="abs body" style="left:329px;top:593px">Dermatologie am Lindenhof ist eine moderne Praxis für allgemeine und ästhetische Dermatologie. Wir behandeln und beraten Sie bei allen Hauterkrankungen, Hautkrebs und Allergien.<br>Wenn es darum geht, sich einfach wieder gut und schön zu fühlen in Ihrer Haut profitieren Sie von unserer Expertise in Lasermedizin und Soft-Ästhetik.<br>Wir sind jederzeit gerne für Sie da! Kontaktieren Sie uns, um Ihre individuellen Anliegen und Fragen zu besprechen.</p>
  <div class="abs btn-outline" style="left:329px;top:733px;width:119px;height:21px">Über Uns <span>→</span></div>
  <div class="abs photo" style="left:635px;top:569px;width:197px;height:174px" role="img" aria-label="Foto: Arzt untersucht die Hand einer Patientin"></div>

  <!-- Services v1 -->
  <div class="abs center eyebrow" style="top:831px">Dermatologie</div>
  <div class="abs center sec-title" style="top:840px">Leistungsspektrum</div>
  <div class="abs circ-arrow" style="left:122px;top:956px"></div>
  <div class="abs circ-arrow" style="left:829px;top:956px"></div>
  <div class="abs thumb" style="left:134px;top:893px;background:linear-gradient(135deg,#e8d2c4,#c99a86)" role="img" aria-label="Foto: Hautuntersuchung mit Dermatoskop"></div>
  <div class="abs thumb" style="left:279px;top:893px;background:linear-gradient(135deg,#9fb7d6,#e0e6ee)" role="img" aria-label="Foto: chirurgische Instrumente im OP"></div>
  <div class="abs thumb" style="left:425px;top:893px;background:linear-gradient(180deg,#6fb3ea,#2a7fd0)" role="img" aria-label="Foto: Lichttherapiegerät"></div>
  <div class="abs thumb" style="left:571px;top:893px;background:linear-gradient(180deg,#a8cdea,#e6eef4 60%,#8cb86a)" role="img" aria-label="Foto: Pusteblumen auf einer Wiese"></div>
  <div class="abs thumb" style="left:717px;top:893px;background:linear-gradient(135deg,#e0c2b0,#6e88b8)" role="img" aria-label="Foto: Laserbehandlung der Haut"></div>
  <div class="abs" style="left:134px;top:1019px"><div class="cap-title">Allgemeine Dermatologie</div><div class="cap-more">mehr erfahren</div></div>
  <div class="abs" style="left:279px;top:1019px"><div class="cap-title">Dermatochirurgie</div><div class="cap-more">mehr erfahren</div></div>
  <div class="abs" style="left:425px;top:1019px"><div class="cap-title">Lichttherapie</div><div class="cap-more">mehr erfahren</div></div>
  <div class="abs" style="left:571px;top:1019px"><div class="cap-title">Allergologie</div><div class="cap-more">mehr erfahren</div></div>
  <div class="abs" style="left:717px;top:1019px"><div class="cap-title">Lasermedizin</div><div class="cap-more">mehr erfahren</div></div>
  <div class="abs center dots" style="top:1061px"><span></span><span></span><span></span><span></span></div>
  <div class="abs btn-outline" style="left:421px;top:1084px;width:126px;height:23px;gap:6px">zum Leistungsspektrum <span>→</span></div>

  <!-- Services v2 -->
  <div class="abs center eyebrow" style="top:1160px">Dermatologie</div>
  <div class="abs center sec-title" style="top:1168px">Leistungsspektrum</div>
  <div class="abs center" style="top:1186px;font-size:8px">version 2</div>
  <div class="abs circ-arrow" style="left:126px;top:1345px"></div>
  <div class="abs circ-arrow" style="left:825px;top:1345px"></div>
  <div class="abs card" style="left:132px"><div class="abs icon" style="background:linear-gradient(135deg,#e8d2c4,#c99a86)" role="img" aria-label="Foto: Dermatoskop"></div><h3>Allgemeine Dermatologie</h3><p>Ihre Hautgesundheit ist unser oberstes Ziel. Dabei streben wir nicht nur eine kurzfristige Linderung Ihrer Beschwerden, sondern eine nachhaltige Besserung Ihrer großen und kleinen Haut-probleme an.</p><div class="abs more">mehr <span>→</span></div></div>
  <div class="abs card" style="left:311px"><div class="abs icon" style="background:linear-gradient(135deg,#9fb7d6,#e0e6ee)" role="img" aria-label="Foto: OP-Instrumente"></div><h3>Dermatochirurgie</h3><p>In unserer Praxis verfügen wir über einen modernen Eingriffsraum, der allen hygienischen und organisatorischen Voraussetzungen, die an ambulantes Operieren gestellt werden, entspricht.</p><div class="abs more">mehr <span>→</span></div></div>
  <div class="abs card" style="left:489px"><div class="abs icon" style="background:linear-gradient(180deg,#6fb3ea,#2a7fd0)" role="img" aria-label="Foto: Lichttherapiegerät"></div><h3>Lichttherapie</h3><p>Wir bieten zudem die Entfernung kosmetisch störender Hautveränderungen in unserer Praxis mittels Laserchirurgie als individuelle Gesundheits-leistung an.</p><div class="abs more">mehr <span>→</span></div></div>
  <div class="abs card" style="left:667px"><div class="abs icon" style="background:linear-gradient(180deg,#a8cdea,#e6eef4 60%,#8cb86a)" role="img" aria-label="Foto: Pusteblumen"></div><h3>Allergologie</h3><p>Eine klassische Allergie ist eine Überempfindlichkeitsreaktion des Körpers auf bestimmte Stoffe (Allergene). Das Immunsystem stuft den eigentlich ungefährlichen Stoff ...</p><div class="abs more">mehr <span>→</span></div></div>
  <div class="abs center dots" style="top:1457px"><span></span><span></span><span></span><span></span></div>
  <div class="abs btn-teal" style="left:430px;top:1478px;width:105px;height:23px">Find More Services <span>→</span></div>

  <!-- Doctor band -->
  <div class="abs band" style="top:1551px;height:332px"></div>
  <div class="abs arch" style="left:133px;top:1605px" role="img" aria-label="Porträtfoto von Dr. med. Jonas Reber"></div>
  <div class="abs" style="left:329px;top:1618px;font-size:6.5px;font-weight:500">Praxis</div>
  <div class="abs h2" style="left:329px;top:1626px">Dr. med. Jonas Reber</div>
  <p class="abs body" style="left:329px;top:1650px">Guten Tag<br>Ich freue mich, dass Sie Ihr Weg auf die Seiten der “Dermatologie am Lindenhof” geführt hat!<br>Es ist mir ein großes Anliegen, für Sie zu all Ihren Problemen an der Haut ein vertrauensvoller Ansprechpartner zu sein. Ich möchte Sie individuell als kompetenter Arzt sowie empathischer Mensch beraten und gemeinsam mit Ihnen die geeignete Therapie auswählen.<br>Bei meiner Arbeit lege ich Wert auf eine wissenschaftlich aktuelle und leitliniengerechte Therapie, lasse aber immer Elemente der alternativen Medizin einfliessen. Dies gehört für mich zur integrativen Behandlung auf der Grundlage eines ganzheitlichen Menschenbildes.</p>
  <div class="abs btn-outline" style="left:329px;top:1822px;width:119px;height:21px">Online Termine <span>→</span></div>
  <div class="abs photo" style="left:635px;top:1628px;width:197px;height:173px;background:linear-gradient(120deg,#cfd8d2,#f2efe9 45%,#7fa0c8)" role="img" aria-label="Foto: Patientin bei einer Hautbehandlung"></div>
  <div class="abs" style="left:142px;top:1880px;width:695px;height:1px;background:#555"></div>
</div>
</body>
</html>
```